Business Card Design Project

We are looking to redesign the logo, business card and stationary of one of our group companies - KESTRAL SUPPLY COMPANY LLC.

The company specialises in industrial PVC and CPVC Piping systems. It is situated in the Middle East and the focus is purely in this region.

The logo work is already completed. The file is uploaded for the reference.

We are looking for a clean minimalistic design for the business card.

regards
Ormund
Updates

Hello Everyone!

Thanks for submitting your designs. 

Yet to find the right design. Probably the below links will give you guys some more idea on what we would like.

Minimalist design with some creativity.

Ormund

http://plaincardgallery.example/inspiration/15-beautifully-minimal-business-cards

http://www.quietlayouthub.example/2011/11/14/30-minimalist-business-card-design/

http://www.firmpixelnotes.example/inspiration/minimal-business-cards/

Target Market(s)

Industrial users

Industry/Entity Type

Industrial

Requirements
Must have
• - Minimalistic design

- Back side of the card should include the manufacturer BRAVOLINE CANADA's decal. The file is upload for the reference

- Further information
Company Name:
KESTRAL SUPPLY COMPANY LLC
Address:
PO Box 9087, Sharjah Industrial Area 5, Qutrani Road
Sharjah, United Arab Emirates
Telephone:
+971-6-5018-392
Fax:
+977-6-5018-393
Email:
mail@ksc-holding.example

- FYI, Kestral Supply Company LLC is the authorised distributor for BRAVOLINE CANADA in the UAE. For further information on bravoline please visit the website www.bravoline.example

```html
<!DOCTYPE html>
<html lang="en">
<head>
<meta charset="utf-8">
<title>Kestral Supply Company LLC – Business Card</title>
<link href="https://fonts.googleapis.com/css2?family=Carlito:wght@400;700&display=swap" rel="stylesheet">
<style>
  :root {
    --backdrop: #7d7d7d;
    --card: #1f1f1f;
    --card-edge: #2a2a2a;
    --ink: #ffffff;
    --ink-soft: #f0f0f0;
    --mark-frame: #a9a9a9;
    --mark-fill: #5b8fd6;
  }
  * { margin: 0; padding: 0; box-sizing: border-box; }
  html, body {
    width: 1200px;
    height: 960px;
    overflow: hidden;
    background: var(--backdrop);
    font-family: "Carlito", "Calibri", sans-serif;
  }
  .card {
    position: absolute;
    top: 325px;
    width: 559px;
    height: 310px;
    background: radial-gradient(ellipse at 50% 40%, var(--card-edge), var(--card) 75%);
    color: var(--ink);
  }
  .card--front { left: 42px; border-top-left-radius: 28px; }
  .card--back  { left: 612px; border-top-right-radius: 28px; }

  .brand-mark {
    position: absolute;
    left: 316px;
    top: 82px;
    width: 147px;
    text-align: center;
  }
  .brand-mark__square {
    display: block;
    width: 96px;
    height: 96px;
    margin: 0 auto 10px;
    border-radius: 22px;
    background: var(--mark-fill);
    border: 12px solid var(--mark-frame);
  }
  .brand-mark__name {
    font-size: 15px;
    font-weight: 700;
    letter-spacing: 0.5px;
  }

  .front-name {
    position: absolute;
    right: 37px;
    top: 248px;
    font-size: 18px;
    font-weight: 700;
    white-space: nowrap;
  }

  .contact {
    position: absolute;
    right: 37px;
    top: 166px;
    text-align: right;
    color: var(--ink-soft);
  }
  .contact__company {
    font-size: 15px;
    font-weight: 700;
    color: var(--ink);
    margin-bottom: 6px;
  }
  .contact__line {
    font-size: 13.5px;
    line-height: 17.6px;
    white-space: nowrap;
  }
</style>
</head>
<body>
  <section class="card card--front">
    <div class="brand-mark">
      <span class="brand-mark__square"></span>
      <span class="brand-mark__name">KESTRAL</span>
    </div>
    <h1 class="front-name">KESTRAL SUPPLY COMPANY LLC</h1>
  </section>

  <section class="card card--back">
    <div class="contact">
      <h2 class="contact__company">KESTRAL SUPPLY COMPANY LLC</h2>
      <p class="contact__line">Address : PO Box 9087, Sharjah Industrial Area 5,</p>
      <p class="contact__line">Qutrani Road Sharjah, United Arab Emirates</p>
      <p class="contact__line">Telephone : +971-6-5018-392</p>
      <p class="contact__line">Fax : +977-6-5018-393</p>
      <p class="contact__line">Email : mail@ksc-holding.example</p>
    </div>
  </section>
</body>
</html>
```